Orbit Field Athletics - "Vuemarq of Sports" design needed

We need a web design created for Orbit Field Athletics. This includes these separate page
The Site map needed has been updated and available to you in Adobe Muse.....
1) Landing Page / Home page
2) Authentication login / Sign up page
3) After logged in - All Content Page
- IE: Vuemarq
4) Once a thumbnail is selected - Content player and other similar content thumbnails
- IE: Vuemarq
4) Generic pages for content fields - terms / policies / contact us / information / etc
5) Generic pages for customer input content fields - My profile / payment / account information / cancellation page
Important for Project Selection.....
A - Design needs to be for Desktop and Mobile.
B - The best example I can point to - that so long as skinned similarly to our
branding at OrbitFieldAthletics is vuemarq.example or KRDV MAX or Tavo
C - Final design needs to be in layered in PSD and AI
D - Attached is our old design that needs an updated concept. Format has been
done in Adobe Muse.

```html
<!DOCTYPE html>
<html lang="en">
<head>
<meta charset="utf-8">
<title>Orbit Field Athletics – User Login</title>
<link rel="stylesheet" href="https://fonts.googleapis.com/css2?family=Open+Sans:ital,wght@0,400;0,600;1,400&display=swap">
<style>
  :root {
    --brand-red: #ed1c24;
    --social-blue: #3b55a8;
    --footer-bg: #222222;
    --white: #ffffff;
    --ink: #222222;
    --field-border: #ececec;
    --placeholder: #c9c9c9;
    --hero-top: #4a5058;
    --hero-mid: #5c636b;
    --hero-low: #3b4047;
  }
  * { box-sizing: border-box; margin: 0; padding: 0; }
  html, body { width: 1200px; height: 820px; overflow: hidden; }
  body {
    position: relative;
    font-family: "Open Sans", Arial, sans-serif;
    background: var(--footer-bg);
    color: var(--ink);
  }
  .hero {
    position: absolute; left: 0; top: 0;
    width: 1200px; height: 692px;
    background:
      radial-gradient(ellipse 420px 300px at 360px 330px, rgba(120,128,140,0.55), transparent 70%),
      radial-gradient(ellipse 380px 260px at 840px 260px, rgba(110,118,128,0.5), transparent 70%),
      linear-gradient(180deg, var(--hero-top) 0%, var(--hero-mid) 45%, var(--hero-low) 100%);
  }
  .brand {
    position: absolute; left: 38px; top: 52px;
    font-size: 22px; font-weight: 600; letter-spacing: 1px;
    color: var(--white);
    line-height: 1.25;
    width: 200px;
  }
  .login-card {
    position: absolute; left: 450px; top: 230px;
    width: 291px; height: 392px;
    background: var(--white);
  }
  .login-card__header {
    height: 57px;
    background: var(--brand-red);
    color: var(--white);
    font-size: 22px;
    line-height: 57px;
    padding-left: 71px;
  }
  .field {
    position: absolute; left: 28px;
    width: 240px; height: 45px;
    border: 2px solid var(--field-border);
    border-radius: 4px;
    display: flex; align-items: center;
    padding-left: 12px;
  }
  .field--email { top: 77px; }
  .field--password { top: 134px; left: 26px; }
  .field svg { flex: none; margin-right: 12px; }
  .field__placeholder {
    font-style: italic; font-size: 14px; color: var(--placeholder);
  }
  .btn {
    position: absolute; left: 26px;
    width: 241px; border-radius: 5px;
    color: var(--white); text-align: center;
  }
  .btn--signin {
    top: 210px; height: 44px; line-height: 44px;
    background: var(--brand-red); font-size: 22px;
  }
  .btn--social {
    top: 263px; height: 42px; line-height: 42px;
    background: var(--social-blue); font-size: 18px; font-weight: 600;
    padding-left: 20px;
  }
  .login-card__signup {
    position: absolute; left: 27px; top: 314px;
    font-size: 14.5px;
  }
  .login-card__forgot {
    position: absolute; left: 26px; top: 341px;
    font-size: 14.5px;
  }
  .link-red { color: var(--brand-red); }
  .site-footer {
    position: absolute; left: 0; top: 692px;
    width: 1200px; height: 128px;
    color: var(--white); text-align: center;
  }
  .site-footer__links {
    position: absolute; left: 0; right: 0; top: 20px;
    font-size: 23px; padding-left: 48px;
  }
  .site-footer__links .sep { margin: 0 14px; }
  .site-footer__copy {
    position: absolute; left: 0; right: 0; top: 71px;
    font-size: 23px; padding-left: 45px;
  }
</style>
</head>
<body>
  <div class="hero" role="img" aria-label="Photograph of a motocross rider performing a freestyle jump against a cloudy sky"></div>

  <div class="brand">ORBIT FIELD ATHLETICS</div>

  <section class="login-card">
    <h1 class="login-card__header" style="font-weight:400">USER LOGIN</h1>

    <div class="field field--email">
      <svg width="22" height="18" viewBox="0 0 22 18" aria-hidden="true">
        <rect x="1" y="1" width="20" height="16" fill="none" stroke="#ed1c24" stroke-width="2"/>
        <path d="M1 1 L11 10 L21 1 M1 17 L8 8 M21 17 L14 8" fill="none" stroke="#ed1c24" stroke-width="2"/>
      </svg>
      <span class="field__placeholder">abcexample@mail.example</span>
    </div>

    <div class="field field--password">
      <svg width="20" height="22" viewBox="0 0 20 22" aria-hidden="true">
        <path d="M5 9 V6 a5 5 0 0 1 10 0 V9" fill="none" stroke="#ed1c24" stroke-width="2.4"/>
        <rect x="1" y="9" width="18" height="12" rx="2" fill="#ed1c24"/>
        <circle cx="6" cy="15" r="1.4" fill="#fff"/>
        <circle cx="10" cy="15" r="1.4" fill="#fff"/>
        <circle cx="14" cy="15" r="1.4" fill="#fff"/>
      </svg>
      <span class="field__placeholder">password goes herre</span>
    </div>

    <div class="btn btn--signin">SIGN IN</div>
    <div class="btn btn--social">Login with Linkspace</div>

    <p class="login-card__signup">New to OrbitGo? <span class="link-red">Sign up now!</span></p>
    <p class="login-card__forgot link-red">Forgot your password?</p>
  </section>

  <footer class="site-footer">
    <nav class="site-footer__links">
      terms of service<span class="sep">|</span>privacy statement<span class="sep">|</span>user agreement<span class="sep">|</span>faq<span class="sep">|</span>help
    </nav>
    <p class="site-footer__copy">©2018 Orbit Field Athletics. All rights reserved</p>
  </footer>
</body>
</html>
```